Pre school dance flyer & Whole Dance Academy Flyer

to design a double sided flyer

one side for pre school pupils aged 18 months to five years

the other side a general whole Academy flyer

We are a dance and Performing Arts Academy
Updates

Reason: I've been very busy at work to focus on this

Target Market(s)

Pre school one side
school age to adult other side
Target is Pre school children side one - school age to adult the other

Industry/Entity Type

School

Font styles to use
Sans Serif

Requirements
Must have
• bright colourful and exciting
Should not have
• dark colours

```html
<!DOCTYPE html>
<html lang="en">
<head>
<meta charset="utf-8">
<title>Brightstep Academy – Free Trial Class Flyer</title>
<link rel="stylesheet" href="https://fonts.googleapis.com/css2?family=Kaushan+Script&family=Damion&family=Oswald:wght@400;500;600&display=swap">
<style>
  :root {
    --bg: #b3b2b3;
    --sky: #00aeef;
    --lime: #b5d334;
    --magenta: #e6007e;
    --sun: #ffd600;
    --ring: #fff200;
    --navy: #2a2b6b;
    --rose: #e4322b;
    --white: #ffffff;
    --ink: #111111;
  }
  * { margin: 0; padding: 0; box-sizing: border-box; }
  html, body { width: 1200px; height: 1200px; overflow: hidden; background: var(--bg); }
  .flyer {
    position: absolute; left: 200px; top: 34px;
    width: 926px; height: 1310px;
    transform: scale(0.8636); transform-origin: top left;
    background: var(--white); overflow: hidden;
    box-shadow: 0 6px 18px rgba(0,0,0,.3);
  }
  .hero { position: absolute; left: 0; top: 0; width: 926px; height: 780px; }
  .hero svg { display: block; }
  .offer {
    position: absolute; left: 42px; top: 425px; color: var(--white);
    font-family: "Kaushan Script", cursive; font-weight: 400; line-height: 1.22;
  }
  .offer .big { font-size: 98px; line-height: 1; }
  .offer .line { font-size: 50px; white-space: nowrap; }
  .cta {
    position: absolute; left: 527px; top: 500px; width: 372px; text-align: center;
    color: var(--white); font-family: "Kaushan Script", cursive; font-weight: 400; font-size: 56px; line-height: 1.15;
  }
  .gallery { position: absolute; left: 0; top: 786px; width: 926px; height: 240px; }
  .gallery .shot { position: absolute; top: 0; height: 240px; }
  .shot.cowgirls { left: 0; width: 322px; background: linear-gradient(135deg, #3a2420, #b23a34 45%, #e8e2de 60%, #2e2a3a); }
  .shot.ballet { left: 332px; width: 318px; background: linear-gradient(160deg, #2a2630, #8c8196 45%, #efeaf2 65%, #4a4552); }
  .shot.garden { left: 660px; width: 266px; background: linear-gradient(180deg, #2b55b8 0%, #2e6ad0 45%, #e79a2c 70%, #2a2a2e 100%); }
  .footer { position: absolute; left: 0; top: 1034px; width: 926px; height: 276px; background: var(--sun); overflow: hidden; }
  .footer .disc { position: absolute; left: 590px; top: -60px; width: 520px; height: 520px; border-radius: 50%; background: var(--white); }
  .welcome {
    position: absolute; left: 34px; top: 14px; white-space: nowrap;
    font-family: "Damion", cursive; font-weight: 400; font-size: 60px; line-height: 1.1; color: var(--rose);
  }
  .details { position: absolute; left: 40px; top: 118px; font-family: "Oswald", sans-serif; font-weight: 500; color: var(--navy); font-size: 21px; line-height: 1.3; text-transform: uppercase; }
  .details .label { color: var(--magenta); }
  .contact { position: absolute; left: 40px; font-family: "Oswald", sans-serif; font-weight: 500; color: var(--navy); font-size: 22px; display: flex; align-items: center; gap: 8px; text-transform: uppercase; }
  .contact.phone { top: 185px; }
  .contact.web { top: 220px; }
  .contact svg { flex: none; }
  .brand { position: absolute; left: 630px; top: 110px; width: 280px; text-align: center; font-family: "Oswald", sans-serif; color: var(--ink); }
  .brand .name { display: flex; align-items: center; justify-content: center; gap: 10px; font-size: 62px; font-weight: 400; line-height: 1; }
  .brand .name .dot { width: 18px; height: 18px; border-radius: 50%; background: var(--magenta); }
  .brand .tag { font-size: 11px; font-weight: 400; letter-spacing: .5px; margin-top: 10px; }
</style>
</head>
<body>
  <main class="flyer">
    <section class="hero">
      <svg width="926" height="780" viewBox="0 0 926 780">
        <defs>
          <linearGradient id="stageGlow" x1="0" y1="0" x2="1" y2="1">
            <stop offset="0" stop-color="#3b2c4e"/>
            <stop offset=".35" stop-color="#e7a9c9"/>
            <stop offset=".6" stop-color="#f4eef2"/>
            <stop offset="1" stop-color="#c8b2de"/>
          </linearGradient>
          <clipPath id="heroClip"><rect width="926" height="780"/></clipPath>
        </defs>
        <g clip-path="url(#heroClip)">
          <rect class="hero-photo" width="926" height="700" fill="url(#stageGlow)" role="img" aria-label="Photo of young ballet pupils in white leotards and tutus performing on stage"/>
          <path d="M300,520 C450,585 610,625 926,410" fill="none" stroke="var(--white)" stroke-width="22"/>
          <path d="M300,545 C450,610 610,650 926,435" fill="none" stroke="var(--sky)" stroke-width="12"/>
          <path d="M300,555 C450,620 610,660 926,445 L926,780 L0,780 L0,560 Z" fill="var(--lime)"/>
          <circle cx="130" cy="650" r="262" fill="none" stroke="var(--white)" stroke-width="10" stroke-dasharray="2 3"/>
          <circle cx="130" cy="650" r="254" fill="var(--sky)"/>
          <ellipse cx="713" cy="610" rx="186" ry="140" fill="var(--magenta)" stroke="var(--ring)" stroke-width="7"/>
        </g>
      </svg>
      <div class="offer">
        <div class="big">Free</div>
        <div class="line">Trial Class</div>
        <div class="line">for all new</div>
        <div class="line">pupils</div>
      </div>
      <div class="cta">Join The<br>Academy<br>Today</div>
    </section>

    <section class="gallery">
      <div class="shot cowgirls" role="img" aria-label="Photo of a group of girls in cowboy hats and red neckerchiefs dancing on stage"></div>
      <div class="shot ballet" role="img" aria-label="Photo of young dancers in white ballet dresses performing with arms outstretched"></div>
      <div class="shot garden" role="img" aria-label="Photo of little dancers in orange tutus with watering cans beside a flower box on stage"></div>
    </section>

    <footer class="footer">
      <div class="disc"></div>
      <h2 class="welcome">We welcome you to Brightstep</h2>
      <p class="details"><span class="label">Venue:</span> The Parish Hall of St Aldric<br>Meadow Lane, Ashby Green, AG4 2LX</p>
      <p class="contact phone">
        <svg width="22" height="22" viewBox="0 0 22 22"><circle cx="11" cy="11" r="9.5" fill="none" stroke="var(--magenta)" stroke-width="2"/><path d="M7.5 6.5l2 0 1 2.5-1.3 1c.7 1.4 1.6 2.3 3 3l1-1.3 2.5 1v2c-4.5.5-8.7-3.7-8.2-8.2z" fill="var(--magenta)"/></svg>
        01632 960 418
      </p>
      <p class="contact web">
        <svg width="22" height="22" viewBox="0 0 22 22" fill="none" stroke="var(--magenta)" stroke-width="1.8"><circle cx="11" cy="11" r="9"/><ellipse cx="11" cy="11" rx="4" ry="9"/><path d="M2 11h18M3.5 6.5h15M3.5 15.5h15"/></svg>
        www.brightstepdanceacademy.co.uk
      </p>
      <div class="brand">
        <div class="name"><span class="dot"></span>Brightstep</div>
        <div class="tag">ACADEMY OF DANCE AND PERFORMING ARTS</div>
      </div>
    </footer>
  </main>
</body>
</html>
```